Brand New Church Business Card Design. Needs to appeal to high school students, professionals.

Business Card. Bold lines and colors. Simple font. This is a new church looking to attract new families who have moved to the area. Business professionals mostly. have a working logo. may need a little tweaking. Church is designed to do excellent ministries for students and children. Like business card design in box on mark vault homepage. Want a front and back side. Prefer colors to match the logo. But will lean on designers preferences and wisdom. DO NOT WANT A CROSS OR RELIGIOUS SYMBOL on the card.

Target Market(s)

Families, Professionals, Students

Industry/Entity Type

High School

Contact Information for Business Card

SaltRock ChurchSaltRock.atForrest Coulter904-515-8349Forrest@PineHollow.at

Font styles to use
Sans Serif

Colors
0255a3
ffffff

Requirements
Must have
• Bold colors. Very Masculine. Creative
Nice to have
• On printnook.markvault.com homepage in the business card design box. the card with the black, blue and gray looks really sharp. matches our logos.
Should not have
• no crosses or religious symbols.

```html
<!DOCTYPE html>
<html lang="en">
<head>
<meta charset="utf-8">
<title>PineHollow Church – Business Card</title>
<link rel="stylesheet" href="https://fonts.googleapis.com/css2?family=PT+Sans:wght@400;700&family=PT+Sans+Narrow:wght@700&display=swap">
<style>
  :root {
    --navy: #022a44;
    --blue: #0a6bbd;
    --card: #f3f3f3;
    --strip: #e4e5e7;
    --ink: #4a4a4a;
    --stage: #3a0a0c;
    --white: #ffffff;
  }
  html, body {
    margin: 0;
    width: 1200px;
    height: 970px;
    overflow: hidden;
    background: var(--stage);
  }
  .canvas { position: relative; width: 1200px; height: 970px; }
  .card {
    position: absolute;
    background: var(--card);
    overflow: hidden;
    font-family: "PT Sans", Arial, sans-serif;
  }
  .card--front { left: 92px; top: 86px; width: 452px; height: 772px; }
  .card--back  { left: 661px; top: 87px; width: 461px; height: 786px; }
  .block { position: absolute; }

  /* front */
  .front-band { left: 53px; top: 346px; width: 399px; height: 81px; background: var(--navy); }
  .front-strip { left: 0; top: 427px; width: 402px; height: 82px; background: var(--strip); }
  .front-url { left: 145px; top: 452px; font-size: 21px; color: var(--ink); }

  .mark-dot {
    position: absolute;
    width: 156px; height: 156px;
    border-radius: 50%;
    background: var(--blue);
  }
  .front .mark-dot { left: 95px; top: 295px; }
  .church-name {
    position: absolute;
    font-family: "PT Sans", Arial, sans-serif;
    font-weight: 700;
    line-height: 1;
    text-align: right;
  }
  .card--front .church-name { left: 150px; top: 352px; width: 232px; font-size: 40px; color: var(--white); }
  .church-name small { display: block; font-size: 28px; margin-top: 2px; }

  /* back */
  .back-rail-top { left: 0; top: 0; width: 46px; height: 501px; background: var(--navy); }
  .back-rail-bottom { left: 0; top: 708px; width: 46px; height: 78px; background: var(--navy); }
  .name-plate {
    left: 155px; top: 120px; width: 306px; height: 54px;
    background: var(--navy); color: var(--white);
    font-family: "PT Sans Narrow", "Arial Narrow", sans-serif;
    font-weight: 700; font-size: 34px;
    display: flex; align-items: center; justify-content: center;
  }
  .card--back .mark-dot { left: 66px; top: 303px; }
  .card--back .church-name { left: 128px; top: 365px; width: 232px; font-size: 40px; color: var(--navy); }

  .contact {
    position: absolute; left: 0; width: 417px; height: 47px;
    background: var(--strip);
    display: flex; align-items: center;
    font-size: 22px; color: var(--ink);
  }
  .contact svg { width: 14px; height: 14px; margin: 0 23px 0 58px; fill: none; stroke: var(--navy); stroke-width: 1.6; }
  .contact--phone { top: 503px; }
  .contact--email { top: 580px; }
  .contact--web   { top: 657px; }
</style>
</head>
<body>
<main class="canvas">
  <section class="card card--front front" aria-label="Card front">
    <div class="block front-band"></div>
    <div class="block front-strip"></div>
    <div class="mark-dot"></div>
    <div class="church-name">PineHollow<small>Church</small></div>
    <div class="block front-url">www.PineHollow.at</div>
  </section>

  <section class="card card--back" aria-label="Card back">
    <div class="block back-rail-top"></div>
    <div class="block back-rail-bottom"></div>
    <div class="block name-plate">Dwayne Pellish</div>
    <div class="mark-dot"></div>
    <div class="church-name">PineHollow<small>Church</small></div>

    <div class="contact contact--phone">
      <svg viewBox="0 0 14 14" aria-hidden="true"><path d="M5 2 Q9 7 5 12" stroke-width="2.4"/></svg>
      904-555-0172
    </div>
    <div class="contact contact--email">
      <svg viewBox="0 0 14 14" aria-hidden="true"><rect x="1" y="3" width="12" height="8"/><path d="M1 3 L7 8 L13 3"/></svg>
      Dwayne@PineHollow.at
    </div>
    <div class="contact contact--web">
      <svg viewBox="0 0 14 14" aria-hidden="true"><circle cx="7" cy="7" r="6"/><ellipse cx="7" cy="7" rx="2.6" ry="6"/><path d="M1 7 H13 M2 4 H12 M2 10 H12"/></svg>
      www.PineHollow.at
    </div>
  </section>
</main>
</body>
</html>
```